International Travel & Visas Firm needs a Schengen Visa eBook Cover Design

We need an ebook cover design for an online based travel, immigration, visas & nationality law firm called 'OrB' (orbit and borderway). We are all about helping people overcome the obstacles to travel and ensuring that people achieve their dreams and ambitions through travel to various destinations and bettering their lives.This initial ebook cover is for our downloaded pdf ebook all about Schengen visas and travelling to any of the 26 European countries that form the Schengen Zone.We want people to be excited about buying this book even before receiving it.We would like to see amazing designs that also speak to our logo and new branding.Check out https://orbitandborderway.example/schengen-visas/ and http://orbitandborderway.pages.funnelvex.example/start-your-schengen-visa-application

Target Market(s)

Travellers that want to get a visa to travel around Europe

Industry/Entity Type

Travel Industry

Colors
fbee3d
faa54b

Requirements
Must have
• - Title:
• Passport Path Primer
Nice to have
• - tagline:
• Unshackle your feet and roam 26 European Countries
• - OrB Logo
• - Reference to it being an insider's guide to Schengen Visas
• - a play on the word OrB (I am)

```html
<!DOCTYPE html>
<html lang="en">
<head>
<meta charset="utf-8">
<title>OrB — Insider's Guide: Passport Path Primer</title>
<link rel="stylesheet" href="https://fonts.googleapis.com/css2?family=Nunito+Sans:wght@300;400;700;800&display=swap">
<style>
  :root {
    --page-bg: #f6f6f6;
    --cover-white: #ffffff;
    --cover-mist: #ececec;
    --brand-orange: #f27636;
    --ink-dark: #3f3f3f;
    --ink-mid: #4a4a4a;
  }
  * { box-sizing: border-box; margin: 0; padding: 0; }
  html, body {
    width: 1200px; height: 900px; overflow: hidden;
    background: var(--page-bg);
    font-family: "Nunito Sans", "Avenir Next", sans-serif;
  }
  .cover {
    position: absolute; left: 300px; top: 20px;
    width: 600px; height: 860px; overflow: hidden;
    background: radial-gradient(circle at 70% 80%, var(--cover-white) 0%, #f4f4f4 45%, var(--cover-mist) 100%);
  }
  .cover-shapes { position: absolute; inset: 0; width: 600px; height: 860px; }
  .brand {
    position: absolute; left: 40px; top: 72px; width: 160px;
    text-align: center;
  }
  .brand-mark {
    display: flex; align-items: center; justify-content: center; gap: 8px;
  }
  .brand-dot {
    width: 16px; height: 16px; border-radius: 50%;
    background: var(--brand-orange);
  }
  .brand-name {
    font-size: 66px; font-weight: 800; line-height: 1;
    color: var(--ink-dark); letter-spacing: -1px;
  }
  .brand-tagline {
    margin-top: 12px; font-size: 11px; font-weight: 800;
    color: var(--ink-dark); white-space: nowrap;
  }
  .kicker {
    position: absolute; left: 0; right: 0; top: 654px;
    padding-left: 24px; text-align: center;
    font-size: 28px; font-weight: 400; line-height: 30px;
    color: var(--ink-mid); letter-spacing: 0.3px;
  }
  .title {
    position: absolute; left: 0; right: 0; top: 684px;
    padding-left: 6px; text-align: center;
    font-size: 52px; font-weight: 800; line-height: 48px;
    color: var(--brand-orange); letter-spacing: 0;
  }
  .tagline {
    position: absolute; left: 0; right: 0; top: 786px;
    font-size: 19px; font-weight: 300; color: var(--ink-mid);
  }
  .tagline-row {
    display: flex; align-items: center; gap: 6px;
    height: 22px; line-height: 22px; white-space: nowrap;
  }
  .tagline-row--first { padding-left: 140px; }
  .tagline-rule { flex: 1; height: 1.5px; background: var(--brand-orange); }
  .tagline-row--second .tagline-rule { flex: 0 0 226px; }
</style>
</head>
<body>
  <main class="cover">
    <svg class="cover-shapes" viewBox="0 0 600 860">
      <defs>
        <linearGradient id="flagTone" x1="0" y1="0" x2="1" y2="1">
          <stop offset="0" stop-color="#f1793a"/>
          <stop offset="0.5" stop-color="#f4853f"/>
          <stop offset="1" stop-color="#f07234"/>
        </linearGradient>
      </defs>
      <ellipse class="flag-disc" cx="227" cy="206" rx="427" ry="384" fill="url(#flagTone)"
        role="img" aria-label="Orange-toned photograph of a waving European flag with stars"/>
      <circle class="logo-disc" cx="100" cy="85" r="227" fill="var(--cover-white)"/>
    </svg>

    <div class="brand">
      <div class="brand-mark">
        <span class="brand-dot"></span>
        <span class="brand-name">OrB</span>
      </div>
      <p class="brand-tagline">orbit and borderway</p>
    </div>

    <p class="kicker">INSIDER’S GUIDE</p>
    <h1 class="title">PASSPORT<br>PATH PRIMER</h1>

    <div class="tagline">
      <div class="tagline-row tagline-row--first">
        <span>Unshackle your feet and roam</span><span class="tagline-rule"></span>
      </div>
      <div class="tagline-row tagline-row--second">
        <span class="tagline-rule"></span><span>26 European Countries</span>
      </div>
    </div>
  </main>
</body>
</html>
```